LEAFNOOK needs a flyer design!

I would like to design a flyer for my small company "LEAFNOOK". We sell stylish and innovative solutions regarding insidegardening in our webshop. We sell modern flowerpots and "green" gifts that you cannot buy in the DIY. Everyone who wants exclusive green design has to buy on our shop. Now we are planning to launch a summer sale flyer in a DIN A5 postcard. In the front we would like to generate attention and state our web-site adress. In the rear of the card we would like to give four to six examples of our products together with the respective discount of 20 to 30%. Our goal is to increase traffic on our website. Please use some of these photos of some of my products if it is useful. I also added my logo "leafnook" and the two logos of my main suppliers "wrenlo" and "claytuftz" that i would like to have named.

Target Market(s)

Hausewives, modern homeowners, restaurants

Industry/Entity Type

It Company

Font styles to use
Sans Serif

Colors

Designer to choose colors to be used in the design.

Requirements
Must have
• Finally i need a text in german language. But we can replace the english text at the end of our project.

```html
<!DOCTYPE html>
<html lang="en">
<head>
<meta charset="utf-8">
<title>LEAFNOOK Summer Sale Flyer</title>
<link rel="stylesheet" href="https://fonts.googleapis.com/css2?family=Fira+Sans+Extra+Condensed:wght@600;700&family=Arimo:wght@400;700&family=Questrial&display=swap">
<style>
  :root {
    --teal: #3f99aa;
    --white: #ffffff;
    --leaf: #8cb03a;
    --ink: #2f2f2f;
    --stage: #ededed;
  }
  * { box-sizing: border-box; margin: 0; padding: 0; }
  html, body { width: 1200px; height: 842px; overflow: hidden; background: var(--stage); }
  .stage { position: relative; width: 1200px; height: 842px; }

  /* Front card */
  .front {
    position: absolute; left: 62px; top: 52px; width: 514px; height: 731px;
    background: var(--teal); overflow: hidden;
  }
  .headline {
    position: absolute; left: 20px; top: 50px; width: 240px;
    font-family: "Fira Sans Extra Condensed", sans-serif; font-weight: 700;
    color: var(--white); text-align: center; font-size: 62px; line-height: 86px;
  }
  .headline .sale { font-size: 66px; }
  .hero-photo {
    position: absolute; left: 252px; top: 38px; width: 226px; height: 432px;
    border-radius: 22px;
    background: linear-gradient(180deg, #f4f4f2 0%, #ecebe7 55%, #e6e3dc 100%);
  }
  .band {
    position: absolute; left: -60px; top: 493px; width: 660px; height: 66px;
    background: var(--white); transform: rotate(-13deg); transform-origin: center;
    display: flex; align-items: center; justify-content: center; gap: 14px;
  }
  .band .brand {
    font-family: "Questrial", sans-serif; font-size: 46px; color: var(--leaf);
    letter-spacing: 1px;
  }
  .band .mark { width: 30px; height: 30px; background: var(--leaf); border-radius: 4px; order: -1; }
  .supplier {
    position: absolute; background: var(--white); border-radius: 8px;
    display: flex; align-items: center; justify-content: center;
    font-family: "Arimo", sans-serif; font-weight: 700; color: var(--ink);
  }
  .supplier.wrenlo { left: 371px; top: 530px; width: 127px; height: 48px; font-size: 26px; }
  .supplier.claytuftz { left: 368px; top: 586px; width: 132px; height: 46px; font-size: 22px; }
  .dates {
    position: absolute; left: 26px; top: 640px; width: 66px; text-align: center;
    font-family: "Arimo", sans-serif; font-weight: 700; color: var(--white);
  }
  .dates .month { font-size: 17px; display: block; }
  .dates .days { font-size: 27px; display: block; line-height: 30px; }
  .divider { position: absolute; left: 100px; top: 634px; width: 2px; height: 58px; background: var(--white); }
  .url {
    position: absolute; left: 116px; top: 648px;
    font-family: "Arimo", sans-serif; font-weight: 700; font-size: 35px; color: var(--white);
  }

  /* Back card */
  .back {
    position: absolute; left: 627px; top: 48px; width: 516px; height: 734px;
    border: 14px solid var(--teal); background: var(--white);
  }
  .tile { position: absolute; }
  .t-cherry { left: 0; top: 0; width: 197px; height: 271px; background: linear-gradient(160deg, #3a3634 0%, #1f2a33 55%, #6b2a30 80%, #c9ccd0 100%); }
  .t-moss-bowl { left: 202px; top: 0; width: 286px; height: 160px; background: linear-gradient(180deg, #8a8a86 0%, #6f6e6a 55%, #3f8a3a 70%, #2a2a2a 100%); }
  .t-kitchen { left: 202px; top: 164px; width: 286px; height: 184px; background: linear-gradient(90deg, #e7e8e6 0%, #d8d8d4 50%, #c9b8a4 80%, #e8e3dc 100%); }
  .t-tray { left: 0; top: 276px; width: 194px; height: 132px; background: linear-gradient(180deg, #3a4048 0%, #51585c 45%, #cfcfc8 70%, #a98b6a 100%); }
  .t-cubes { left: 239px; top: 338px; width: 249px; height: 200px; border: 3px solid var(--white); background: linear-gradient(180deg, #d9d9d7 0%, #c8c8c4 40%, #6a8e3e 60%, #a8a8a4 100%); }
  .t-orchids { left: 0; top: 412px; width: 237px; height: 204px; background: linear-gradient(180deg, #e4e7ea 0%, #cdd3d8 45%, #b03a5c 62%, #ece8e2 80%, #b89572 100%); }
  .t-grass-tall { left: 281px; top: 542px; width: 207px; height: 164px; background: linear-gradient(180deg, #f1f1f1 0%, #7aa33a 30%, #f4f4f4 55%, #e8e8e8 100%); }
  .t-grass-low { left: 0; top: 620px; width: 277px; height: 86px; background: linear-gradient(180deg, #f2f2f2 0%, #6f9a34 45%, #f5f5f5 80%, #dcdcdc 100%); }

  .tagline {
    position: absolute; left: 14px; top: 10px; width: 462px; height: 28px;
    background: var(--white); border-radius: 6px;
    font-family: "Arimo", sans-serif; font-weight: 700; font-size: 14px; color: var(--ink);
    display: flex; align-items: center; justify-content: center;
  }
  .badge {
    position: absolute; background: var(--white); border-radius: 10px;
    font-family: "Arimo", sans-serif; color: var(--ink); text-align: center;
    display: flex; flex-direction: column; justify-content: center; font-size: 10px; line-height: 12px;
  }
  .badge strong { font-size: 14px; line-height: 18px; }
  .badge.off-15 { left: 149px; top: 223px; width: 78px; height: 75px; }
  .badge.off-20 { left: 221px; top: 542px; width: 76px; height: 93px; }
  .badge.limited { left: 407px; top: 110px; width: 80px; height: 78px; font-size: 10px; line-height: 13px; }
  .badge.limited b { font-weight: 700; }
</style>
</head>
<body>
<main class="stage">
  <section class="front">
    <h1 class="headline">most<br>awaited<br>online<br>summer<br><span class="sale">SALE !</span></h1>
    <div class="hero-photo" role="img" aria-label="Upside-down hanging planters in green and blue with trailing plants against a white brick wall"></div>
    <div class="band"><span class="brand">LEAFNOOK</span><span class="mark"></span></div>
    <div class="supplier wrenlo">wrenlo</div>
    <div class="supplier claytuftz">claytuftz</div>
    <p class="dates"><span class="month">July</span><span class="days">2 - 8</span></p>
    <span class="divider"></span>
    <p class="url">www.leafnook.de</p>
  </section>

  <section class="back">
    <div class="tile t-cherry" role="img" aria-label="Glossy red ceramic cherry decoration on a table"></div>
    <div class="tile t-moss-bowl" role="img" aria-label="Black bowl planter filled with green moss beside a pepper mill"></div>
    <div class="tile t-kitchen" role="img" aria-label="Bright kitchen with hanging upside-down planters"></div>
    <div class="tile t-tray" role="img" aria-label="Long white tray planter with silver grass"></div>
    <div class="tile t-orchids" role="img" aria-label="White square pots with pink orchids"></div>
    <div class="tile t-cubes" role="img" aria-label="Grey cube planters with white hydrangeas on a terrace"></div>
    <div class="tile t-grass-tall" role="img" aria-label="Tall white planter with green grass"></div>
    <div class="tile t-grass-low" role="img" aria-label="Low white planter with green grass"></div>

    <p class="tagline">Design discoveries, gift ideas, flowers and plants, and much more!</p>
    <div class="badge limited"><span>Summer <b>SALE</b></span><span><b>LIMITED</b> time</span><span>only !</span></div>
    <div class="badge off-15"><strong>15% OFF</strong><span>on</span><span>SELECTED</span><span>items</span></div>
    <div class="badge off-20"><strong>20% OFF</strong><span>on</span><span>SELECTED</span><span>items</span></div>
  </section>
</main>
</body>
</html>
```